Business cards for Norwegian software consultancy business

We are in need of business cards for our Norwegian consultancy company.
“Talvik Brensor AS” specializes in software development, architecture and agile methodology, providing mostly on-site services at customers.
The cards should reflect a certain level of business professionalism with an elegant touch, while paying tribute to our modern and technological heritage. Our logo should be featured, as well as room for basic information about the cardholder and legal information of the company (company name, address and VAT number).
We would like our cards to reflect that we are a modern consulting company. It should present a professional image that people will remember. The texture and color pallette should reflect our professionalism and reliability, so we prefer a light color pallette with colors such as gray, white, blue and black. The number of colors used should however not be overwhelming, with the text being distinct and readable.
We are open to untraditional layouts and playful designs as long as they communicate the intent stated above.
You could also take a look at our website http://www.brensor.no for input on our visual profile.
Our logo is attached in the form of vectors and rasterized PNG. Please comment if you would like the black-white and/or inverted versions as well.
Architecture
Company information:
Talvik Brensor AS
Lindeholtveien 7, 3142 Vestskogen
461 82 915
info@brensor.no
www.brensor.no
Employee information:
Full name
Title
Email
Phone

```html
<!DOCTYPE html>
<html lang="no">
<head>
<meta charset="utf-8">
<title>Talvik Brensor AS – Business Card</title>
<link rel="stylesheet" href="https://fonts.googleapis.com/css2?family=Cabin+Condensed:wght@400;600;700&display=swap">
<style>
  :root {
    --canvas-bg: #dcd9d5;
    --card-bg: #ececec;
    --ink: #1e1e1e;
    --ink-soft: #3a3a3a;
    --accent: #4a8cc4;
    --rule: #6b6b6b;
    --tile-light: #dedede;
    --tile-mid: #d3d3d3;
  }
  * { margin: 0; padding: 0; box-sizing: border-box; }
  html, body {
    width: 1200px;
    height: 712px;
    overflow: hidden;
    background: var(--canvas-bg);
    font-family: "Cabin Condensed", "Arial Narrow", sans-serif;
    color: var(--ink);
  }
  .card {
    position: absolute;
    left: 100px;
    top: 70px;
    width: 1000px;
    height: 572px;
    background: var(--card-bg);
    box-shadow: 0 4px 14px rgba(0,0,0,0.18);
    overflow: hidden;
  }
  .card__texture {
    position: absolute;
    right: 0;
    top: 0;
    width: 520px;
    height: 420px;
    background: radial-gradient(ellipse at 70% 35%, var(--tile-mid) 0%, var(--tile-light) 45%, rgba(236,236,236,0) 75%);
  }
  .brand {
    position: absolute;
    left: 70px;
    top: 150px;
    display: flex;
    align-items: center;
    gap: 18px;
  }
  .brand__mark {
    width: 34px;
    height: 34px;
    background: var(--accent);
  }
  .brand__name {
    font-size: 54px;
    font-weight: 400;
    letter-spacing: 2px;
    color: var(--ink);
    text-transform: uppercase;
    line-height: 1;
  }
  .holder {
    position: absolute;
    left: 110px;
    top: 338px;
    text-transform: uppercase;
  }
  .holder__name {
    font-size: 30px;
    font-weight: 700;
    letter-spacing: 1px;
    line-height: 1;
  }
  .holder__title {
    margin-top: 6px;
    font-size: 15px;
    font-weight: 700;
    letter-spacing: 0.5px;
    color: var(--ink-soft);
  }
  .address {
    position: absolute;
    left: 560px;
    top: 236px;
    font-size: 17px;
    line-height: 1.35;
    text-transform: uppercase;
    color: var(--ink-soft);
  }
  .divider {
    position: absolute;
    left: 556px;
    top: 298px;
    width: 1.5px;
    height: 150px;
    background: var(--rule);
  }
  .contacts {
    position: absolute;
    left: 578px;
    top: 312px;
    list-style: none;
  }
  .contacts__item {
    display: flex;
    align-items: center;
    gap: 14px;
    height: 28px;
    font-size: 17px;
    text-transform: uppercase;
    color: var(--ink-soft);
  }
  .contacts__icon {
    width: 16px;
    height: 16px;
    flex: none;
  }
  .contacts__icon path, .contacts__icon rect, .contacts__icon circle {
    fill: none;
    stroke: var(--accent);
    stroke-width: 1.6;
  }
  .contacts__icon .solid { fill: var(--accent); stroke: none; }
</style>
</head>
<body>
  <main class="card">
    <div class="card__texture" role="img" aria-label="Soft grey tiled square pattern in the upper right corner"></div>

    <div class="brand">
      <span class="brand__mark"></span>
      <span class="brand__name">Talvik Brensor</span>
    </div>

    <div class="holder">
      <p class="holder__name">Eirik Solhaug</p>
      <p class="holder__title">President &amp; CEO</p>
    </div>

    <p class="address">Lindeholtveien 7,<br>3142 Vestskogen</p>

    <span class="divider"></span>

    <ul class="contacts">
      <li class="contacts__item">
        <svg class="contacts__icon" viewBox="0 0 16 16"><path class="solid" d="M2 6c0-2 3-3 6-3s6 1 6 3l-3 1-1-2H6L5 7zM4 8h8l1 5H3z"/></svg>
        461 82 915
      </li>
      <li class="contacts__item">
        <svg class="contacts__icon" viewBox="0 0 16 16"><rect x="4.5" y="1.5" width="7" height="13" rx="1.2"/><circle class="solid" cx="8" cy="12" r="0.9"/></svg>
        +47 912 40 683
      </li>
      <li class="contacts__item">
        <svg class="contacts__icon" viewBox="0 0 16 16"><rect x="1.5" y="3.5" width="13" height="9"/><path d="M1.5 3.5 8 9l6.5-5.5"/></svg>
        eirik@brensor.no
      </li>
      <li class="contacts__item">
        <svg class="contacts__icon" viewBox="0 0 16 16"><circle cx="8" cy="8" r="6.5"/><path d="M1.5 8h13M8 1.5c-3 3.5-3 9.5 0 13M8 1.5c3 3.5 3 9.5 0 13"/></svg>
        www.brensor.no
      </li>
    </ul>
  </main>
</body>
</html>
```